BUSINESS book cover

Publishing a book for a specific industry and hope to customize it for different industries in the future. So, design needs to be flexible. I want BRIGHT (possibly orange) cover with large words for title...really do not need illustration. Just the subtitle will change for future editions. Book is going to be 5.25" x 8"

Sorry for any confusion. The title of the book is: "Once You Reach a Yes..." The subtitle is: A Comprehensive Member Expderience Guide for Today's Club Management Professional

```html
<!DOCTYPE html>
<html lang="en">
<head>
<meta charset="utf-8">
<title>Once You Reach a Yes... — Book Cover</title>
<link rel="stylesheet" href="https://fonts.googleapis.com/css2?family=Anton&family=PT+Sans+Narrow:wght@400;700&display=swap">
<style>
  :root {
    --orange: #fb7b29;
    --orange-deep: #e8620f;
    --orange-shade: #d9590c;
    --paper: #ffffff;
    --ink: #111111;
    --subtitle-ink: #2b2118;
    --photo-light: #bdbdbd;
    --photo-dark: #4a4a4a;
  }
  * { margin: 0; padding: 0; box-sizing: border-box; }
  html, body { width: 1200px; height: 793px; overflow: hidden; background: var(--paper); }

  .cover { position: relative; width: 1200px; height: 793px; overflow: hidden; }

  .back-page {
    position: absolute; left: 0; top: 0; width: 580px; height: 655px;
    background: linear-gradient(to right, var(--paper) 0%, var(--paper) 88%, #e6e6e6 97%, #cfcfcf 100%);
  }
  .front-page {
    position: absolute; left: 628px; top: 0; width: 572px; height: 655px;
    background: linear-gradient(to right, #d6d6d6 0%, #f1f1f1 5%, var(--paper) 12%);
  }
  .spine {
    position: absolute; left: 580px; top: 0; width: 48px; height: 793px;
    background: linear-gradient(to right, var(--orange-shade), var(--orange-deep) 30%, var(--orange-deep) 70%, var(--orange-shade));
  }
  .band {
    position: absolute; top: 655px; height: 138px;
  }
  .band--back {
    left: 0; width: 580px;
    background: linear-gradient(to right, var(--orange) 0%, var(--orange) 85%, var(--orange-shade) 100%);
  }
  .band--front {
    left: 628px; width: 572px;
    background: linear-gradient(to right, var(--orange-shade) 0%, var(--orange) 10%);
  }

  .blurb {
    position: absolute; left: 62px; top: 90px; width: 470px;
    font-family: "PT Sans Narrow", "Arial Narrow", sans-serif;
    font-size: 14px; line-height: 15.2px; color: var(--ink);
  }
  .blurb p { margin: 0; }
  .blurb ul { list-style: none; }
  .blurb li { position: relative; padding-left: 37px; }
  .blurb li::before { content: "▪"; position: absolute; left: 0; font-size: 9px; }

  .author-photo { position: absolute; left: 25px; top: 487px; width: 210px; height: 140px; }

  .author-bio {
    position: absolute; left: 248px; top: 481px; width: 300px;
    font-family: "PT Sans Narrow", "Arial Narrow", sans-serif;
    font-size: 14px; line-height: 15.2px; color: var(--ink);
  }

  .title {
    position: absolute; left: 628px; top: 78px; width: 572px;
    font-family: "Anton", "Impact", sans-serif; color: var(--orange);
    text-align: center; text-transform: uppercase; font-weight: 400;
  }
  .title span { display: block; letter-spacing: -1px; }
  .title .line-xl { font-size: 172px; line-height: 152px; }
  .title .line-md { font-size: 80px; line-height: 86px; margin-top: 8px; }
  .title .line-last { font-size: 172px; line-height: 160px; }

  .subtitle {
    position: absolute; left: 700px; top: 682px; width: 452px;
    font-family: "Anton", "Impact", sans-serif; font-weight: 400;
    font-size: 22px; line-height: 26px; text-align: center; color: var(--subtitle-ink);
  }
</style>
</head>
<body>
<main class="cover">
  <section class="back-page">
    <div class="blurb">
      <p>This book is for club management professionals only!</p>
      <p>Why is Brewline Café so successful in selling you a $4.00 cup of coffee when QuickCup Diner charges $2.00?</p>
      <p>Why does a stay at a Grand Meridian hotel seem much different than at a stay at the Wayside Lodge?</p>
      <p>Most people today would answer that it’s all about ‘customer service’ when, in fact, they would be wrong! Both QuickCup Diner and Wayside Lodge offer incredible customer service. What Brewline Café and Grand Meridian understand is that it is about the customer EXPERIENCE!</p>
      <p>Much attention is given to the member experience in this profession, but do we really understand what needs to be done to take our club to the next level? “Once You Reach a Yes...” is a comprehensive book with assessments, surveys and examples personalized to the club management profession.</p>
      <p>In reading this book, you will be able to:</p>
      <ul>
        <li>Analyze and tweak our member touch points</li>
        <li>Create a “touch point map” specific to your club</li>
        <li>Assess whether or not your strategy will be successful</li>
        <li>Be more innovative in managing your people and your members</li>
        <li>Take an innovation survey</li>
        <li>Establish your club’s “Declaration of Experience”</li>
        <li>Distinguish between employee engagement and employee satisfaction</li>
      </ul>
      <p>And much, much more</p>
    </div>

    <svg class="author-photo" role="img" aria-label="Black and white portrait photo of the author" viewBox="0 0 210 140">
      <defs>
        <linearGradient id="portraitTone" x1="0" y1="0" x2="1" y2="1">
          <stop offset="0" stop-color="var(--photo-light)"/>
          <stop offset="1" stop-color="var(--photo-dark)"/>
        </linearGradient>
      </defs>
      <rect width="210" height="140" fill="url(#portraitTone)"/>
    </svg>

    <p class="author-bio">Mark Devlin M.Ed, CSP has been working with club professionals for 15+ years. His first book, “Thinking Past the Edges” has long been an industry favorite and his sessions at NCMF nationally and for individual clubs have made him a leading expert in creative thinking as it applies to the member experience. For more information on booking Mark, visit www.MarkDevlin.com or call him directly at 555-014-2287</p>
  </section>

  <div class="band band--back"></div>
  <div class="spine"></div>

  <section class="front-page"></section>
  <div class="band band--front"></div>

  <h1 class="title">
    <span class="line-xl">Once</span>
    <span class="line-xl">You</span>
    <span class="line-md">Reach a</span>
    <span class="line-last">Yes</span>
  </h1>

  <p class="subtitle">A Comprehensive Member Expderience Guide for Today's Club Management Professional</p>
</main>
</body>
</html>
```